Clean and modern business cards

Looking for an updated business card design for my dental office “corvanta dental” . Looking for a modern clean / sleek design . I’m thinking black background but open to seeing other options . One side needs to have an appointment card . Card needs to have logo, dentist name , phone, email , address . I’ve attached couple of cards I thought were cool as well as my logo
Target Market(s)
Dental patients
Industry/Entity Type
Dentistry
Contact Information for Business Card
Phone email address

```html
<!DOCTYPE html>
<html lang="en">
<head>
<meta charset="UTF-8">
<title>Corvanta Dental — Business &amp; Appointment Card</title>
<link rel="stylesheet" href="https://fonts.googleapis.com/css2?family=Montserrat:wght@400;500;700;800&display=swap">
<style>
  :root {
    --page-bg: #ffffff;
    --card-bg: #000000;
    --ink: #ffffff;
    --ink-soft: #e6e6e6;
    --rule: #cfcfcf;
    --art-light: #8a8a8a;
    --art-dark: #3a3a3a;
  }
  * { box-sizing: border-box; margin: 0; padding: 0; }
  html, body {
    width: 1019px;
    height: 1200px;
    overflow: hidden;
    background: var(--page-bg);
  }
  body {
    font-family: "Montserrat", Arial, sans-serif;
    color: var(--ink);
  }
  .card-set {
    position: absolute;
    top: 287px;
    left: 80px;
    display: flex;
    gap: 60px;
  }
  .card {
    position: relative;
    width: 400px;
    height: 625px;
    background: var(--card-bg);
  }

  /* Front */
  .brand {
    position: absolute;
    top: 52px;
    right: 32px;
    text-align: right;
    font-weight: 800;
    line-height: 1.05;
  }
  .brand-name { font-size: 27px; letter-spacing: 0.5px; display: block; }
  .brand-sub { font-size: 13px; letter-spacing: 3px; display: block; }
  .hero-art {
    position: absolute;
    left: 60px;
    top: 252px;
    width: 280px;
    height: 270px;
    border-radius: 50%;
    background: radial-gradient(circle at 50% 48%, var(--art-dark) 0 28%, var(--art-light) 40%, rgba(138,138,138,0.55) 62%, rgba(0,0,0,0) 72%);
  }
  .dentist {
    position: absolute;
    left: 0;
    right: 0;
    top: 500px;
    text-align: center;
  }
  .dentist-name {
    font-size: 18px;
    font-weight: 800;
    letter-spacing: 2.6px;
  }
  .dentist-contact {
    margin-top: 8px;
    font-size: 10.5px;
    letter-spacing: 1.6px;
    line-height: 1.8;
    color: var(--ink-soft);
  }

  /* Back */
  .appointment {
    position: absolute;
    left: 40px;
    top: 118px;
    right: 30px;
  }
  .appointment-title {
    font-size: 17px;
    font-weight: 500;
    letter-spacing: 3px;
  }
  .field {
    display: flex;
    align-items: flex-end;
    margin-top: 27px;
    font-size: 15px;
    font-weight: 700;
    letter-spacing: 3px;
  }
  .field-line {
    width: 176px;
    margin-left: 8px;
    border-bottom: 1px solid var(--rule);
    height: 14px;
  }
  .notice {
    position: absolute;
    left: 40px;
    top: 406px;
    font-size: 17.5px;
    font-weight: 500;
    letter-spacing: 3px;
    line-height: 40px;
  }
</style>
</head>
<body>
  <main class="card-set">
    <section class="card card-front" aria-label="Business card front">
      <div class="brand">
        <span class="brand-name">CORVANTA</span>
        <span class="brand-sub">DENTAL</span>
      </div>
      <div class="hero-art" role="img" aria-label="Grey cluster of soft bubbles surrounding a dark tooth silhouette"></div>
      <div class="dentist">
        <p class="dentist-name">DR. ELIAN VARKO</p>
        <p class="dentist-contact">(204) 555-0192 &nbsp;|&nbsp; HELLO@CORVANTADENTAL.CA<br>2480 LARKFIELD AVE, WINNIPEG, MB</p>
      </div>
    </section>

    <section class="card card-back" aria-label="Appointment card back">
      <div class="appointment">
        <p class="appointment-title">your next appointment is</p>
        <p class="field">date:<span class="field-line"></span></p>
        <p class="field">time:<span class="field-line"></span></p>
      </div>
      <p class="notice">To cancel or reschedule<br>please notify us at least<br>48 hours prior to your<br>scheduled appointment</p>
    </section>
  </main>
</body>
</html>
```